High end Electrical/home automation Business Card

Need a card for a high end electrical and home automation company utilising the existing logo.
Phone
Email
Website

Like black look with raised detail. Don’t necessarily need to keep colour of logo it could be made grayscale or white etc

Target Market(s)

High end clients

Contact Information for Business Card

Northwell Electrical

Requirements
Must have
• Logo, phone, email, website, address

High end look
Nice to have
• Black background card
Raised font
Should not have
• Lots of colour

```html
<!DOCTYPE html>
<html lang="en">
<head>
<meta charset="utf-8">
<title>Northwell Electrical – Business Card</title>
<link href="https://fonts.googleapis.com/css2?family=Montserrat:wght@400;500;700&display=swap" rel="stylesheet">
<style>
  :root {
    --backdrop: #1b1b1d;
    --card: #38383b;
    --paper: #ffffff;
    --accent: #1a8fd6;
    --text-light: #ffffff;
    --text-dark: #2b2b2e;
  }
  * { box-sizing: border-box; margin: 0; padding: 0; }
  html, body {
    width: 1200px; height: 900px; overflow: hidden;
    background: var(--backdrop);
    font-family: "Montserrat", sans-serif;
  }
  .sheet {
    width: 1200px; height: 900px;
    display: flex; flex-direction: column; align-items: center; justify-content: center;
    gap: 40px;
  }
  .card {
    position: relative;
    width: 700px; height: 400px;
    border-radius: 28px;
    background: var(--card);
    overflow: hidden;
    box-shadow: 0 18px 40px rgba(0,0,0,0.55);
  }
  .brand {
    display: flex; align-items: center; gap: 14px;
    font-weight: 700; letter-spacing: 0.5px;
  }
  .brand-dot {
    width: 22px; height: 22px; border-radius: 50%;
    background: var(--accent);
  }
  .card-front .brand {
    position: absolute; inset: 0; justify-content: center;
    color: var(--text-light); font-size: 44px;
  }
  .card-back .contact {
    position: absolute; left: 52px; top: 70px;
    color: var(--text-light);
  }
  .contact-name {
    color: var(--accent); font-size: 27px; font-weight: 500;
    letter-spacing: 3px; text-transform: uppercase;
  }
  .contact-role { font-size: 18px; margin-top: 4px; }
  .contact-address { font-size: 17px; line-height: 1.4; margin-top: 26px; letter-spacing: 0.5px; }
  .contact-lines { list-style: none; margin-top: 10px; font-size: 17px; line-height: 1.5; letter-spacing: 0.5px; }
  .contact-lines li { display: flex; align-items: center; gap: 10px; }
  .contact-lines svg { width: 14px; height: 14px; flex: none; }
  .back-panel {
    position: absolute; left: 400px; top: 24px;
    width: 560px; height: 560px; border-radius: 50%;
    background: var(--paper);
    border: 5px solid transparent;
    border-left-color: var(--accent);
    border-top-color: var(--accent);
    transform: rotate(-10deg);
  }
  .card-back .brand {
    position: absolute; left: 440px; top: 170px; width: 240px;
    flex-wrap: wrap; justify-content: center; text-align: center;
    color: var(--text-dark); font-size: 30px; line-height: 1.15;
  }
</style>
</head>
<body>
<main class="sheet">
  <section class="card card-front">
    <div class="brand"><span class="brand-dot"></span>Northwell Electrical</div>
  </section>

  <section class="card card-back">
    <div class="contact">
      <h1 class="contact-name">Daniel Carter</h1>
      <p class="contact-role">Founder</p>
      <p class="contact-address">418 Harbor Lane<br>Fairview, WA 98012</p>
      <ul class="contact-lines">
        <li>
          <svg viewBox="0 0 24 24" aria-hidden="true"><path fill="var(--accent)" d="M6.6 10.8a15 15 0 0 0 6.6 6.6l2.2-2.2c.3-.3.7-.4 1-.2 1.1.4 2.3.6 3.6.6.6 0 1 .4 1 1V20c0 .6-.4 1-1 1A17 17 0 0 1 3 4c0-.6.4-1 1-1h3.5c.6 0 1 .4 1 1 0 1.3.2 2.5.6 3.6.1.3 0 .7-.2 1z"/></svg>
          555 014 2286
        </li>
        <li>
          <svg viewBox="0 0 24 24" aria-hidden="true"><rect x="2.5" y="5" width="19" height="14" rx="1.5" fill="none" stroke="var(--accent)" stroke-width="2"/><path d="M3 6l9 7 9-7" fill="none" stroke="var(--accent)" stroke-width="2"/></svg>
          hello@northwellelectric.com
        </li>
        <li>
          <svg viewBox="0 0 24 24" aria-hidden="true"><circle cx="12" cy="12" r="9.5" fill="none" stroke="var(--accent)" stroke-width="2"/><path d="M2.5 12h19M12 2.5c3 3 3 16 0 19M12 2.5c-3 3-3 16 0 19" fill="none" stroke="var(--accent)" stroke-width="1.6"/></svg>
          northwellelectric.com
        </li>
      </ul>
    </div>
    <div class="back-panel"></div>
    <div class="brand"><span class="brand-dot"></span>Northwell Electrical</div>
  </section>
</main>
</body>
</html>
```